Business Card Design for Occupational Medicine Start Up Company

We need to design a professional business card. We are a healthcare company providing occupational medicine services to blue collar industries. We are professional, efficient and high quality service providers.

Target Market(s)

Blue Collar Industry: Shipbuilding, Ports, Trucking Companies; The Executives and Safety Officers for these companies

Industry/Entity Type

Healthcare

Contact Information for Business Card

Logo, Name, Title, Email, Phone

Other font styles liked:
• Please match our Brand Guide

Requirements
Must have
• Our Company Colors and Logo

```html
<!DOCTYPE html>
<html lang="en">
<head>
<meta charset="utf-8">
<title>Crewline Health – Business Card</title>
<link href="https://fonts.googleapis.com/css2?family=Montserrat:wght@600;700&family=Open+Sans:wght@400;600;700&display=swap" rel="stylesheet">
<style>
  :root {
    --backdrop: #262626;
    --card: #1b1b1c;
    --card-edge: #2a2a2b;
    --white: #ffffff;
    --muted: #a9a9a9;
    --rule: #5a5a5a;
    --pattern-a: #161617;
    --pattern-b: #232324;
  }
  * { margin: 0; padding: 0; box-sizing: border-box; }
  html, body {
    width: 1200px; height: 1108px; overflow: hidden;
    background: var(--backdrop);
  }
  .stage {
    position: relative; width: 1200px; height: 1108px;
    display: flex; justify-content: center; align-items: center; gap: 70px;
  }
  .card {
    position: relative; width: 420px; height: 680px;
    background: var(--card); border-radius: 30px;
    box-shadow: 0 18px 40px rgba(0,0,0,.45);
    overflow: hidden;
  }
  /* back side */
  .card-back .pattern {
    position: absolute; inset: 0;
    background: linear-gradient(160deg, var(--pattern-b) 0%, var(--pattern-a) 45%, var(--pattern-b) 100%);
  }
  .wordmark {
    font-family: "Montserrat", sans-serif; font-weight: 700;
    color: var(--white); text-transform: uppercase; letter-spacing: .5px;
    display: flex; align-items: center; gap: 10px;
  }
  .wordmark .dot {
    width: 12px; height: 12px; border-radius: 50%; background: var(--white);
  }
  .card-back .wordmark {
    position: absolute; left: 42px; top: 470px; font-size: 28px;
  }
  /* front side */
  .card-front {
    display: flex; flex-direction: column; align-items: center;
    padding-top: 120px; text-align: center;
    font-family: "Open Sans", sans-serif;
  }
  .card-front .wordmark { font-size: 32px; flex-direction: column; gap: 14px; }
  .card-front .wordmark .dot { width: 46px; height: 46px; }
  .person-name {
    margin-top: 44px; font-weight: 700; font-size: 30px; color: var(--white);
    letter-spacing: .5px; text-transform: uppercase;
  }
  .rule { width: 300px; height: 1px; background: var(--rule); }
  .person-name + .rule { margin-top: 8px; }
  .person-title { margin-top: 6px; font-size: 17px; color: var(--muted); }
  .icons { display: flex; gap: 6px; margin: 8px 0 10px; }
  .icon {
    width: 30px; height: 30px; background: var(--white); border-radius: 4px;
    display: flex; align-items: center; justify-content: center;
  }
  .contact { margin-top: 14px; font-size: 18px; line-height: 28px; color: var(--muted); }
  .contact + .rule { margin-top: 14px; }
  .address { margin-top: 12px; font-size: 18px; line-height: 26px; color: var(--muted); }
  .address + .rule { margin-top: 14px; }
</style>
</head>
<body>
<main class="stage">
  <section class="card card-back">
    <div class="pattern" role="img" aria-label="Faint repeating brand symbol pattern across the card back"></div>
    <div class="wordmark"><span class="dot"></span>Crewline Health</div>
  </section>

  <section class="card card-front">
    <div class="wordmark"><span class="dot"></span>Crewline Health</div>
    <h1 class="person-name">Dale Hartley</h1>
    <div class="rule"></div>
    <p class="person-title">Manager</p>
    <div class="icons">
      <span class="icon">
        <svg width="18" height="18" viewBox="0 0 24 24" fill="none" stroke="#1b1b1c" stroke-width="2" stroke-linecap="round" stroke-linejoin="round"><path d="M6.6 3h3l1.5 4.5-2 1.5a11 11 0 0 0 5.9 5.9l1.5-2 4.5 1.5v3a2 2 0 0 1-2 2A16 16 0 0 1 4.6 5a2 2 0 0 1 2-2z"/></svg>
      </span>
      <span class="icon">
        <svg width="18" height="18" viewBox="0 0 24 24" fill="none" stroke="#1b1b1c" stroke-width="2" stroke-linejoin="round"><rect x="3" y="5" width="18" height="14" rx="1"/><path d="M3 6l9 7 9-7"/></svg>
      </span>
      <span class="icon">
        <svg width="18" height="18" viewBox="0 0 24 24" fill="none" stroke="#1b1b1c" stroke-width="1.8"><circle cx="12" cy="12" r="9"/><ellipse cx="12" cy="12" rx="4" ry="9"/><path d="M3 12h18M5 7h14M5 17h14"/></svg>
      </span>
    </div>
    <div class="rule"></div>
    <p class="contact">214-555-0182<br>info@crewlinehealth.com<br>www.crewlinehealth.com</p>
    <div class="rule"></div>
    <p class="address">4410 Dockside Ave. Suite 210<br>Dallas, TX 0000</p>
    <div class="rule"></div>
  </section>
</main>
</body>
</html>
```